Scientific project description

Here is a project description related to cellular mechanics, showing above the forces acting on cells in the tissues of our body. The forces on single cells are there to depict how forces are acting on cells (pressure squeezes the cell, shear flow is pushing the upward parts of the cell, tension pulls one part of the cell, strain is stretching the whole cell; the single cell images are to be found also on the last page). Intense red/purple are used to indicate that the forces are stressful (the colors to be used do not need to be exactly like these colors). The picture in the middle is a view of cells (same picture on next page if that needs to be modified). At the left, a description of what happens when everything is going well, i.e. the body stays healthy. At the right, if you dysfunction you get disease. Green nuances were used to indicate health, brownish, perhaps not so pleasant nuances were used to indicate disease. Below are the steps of the project.

On the whole, we're rather happy with the concept description as such, but it should look a little bit nicer. To many color nuances give a "noisy" impression, fonts could be nicer, layout more crisp, and the text on the steps should be more readable. We would also like to have two versions of the same picture, one with black background, one with white.

Target Market(s)

Scientists that are evaluating our project

Requirements
Must have
• Easy to grasp the idea, easy to read and understand the underlying idea.
Nice to have
• Would be good to have the Concept title ("Pelvoran Concept and Envisioned Project Progression) on top of the figure as indicated in the second brief picture submitted.

```html
<!DOCTYPE html>
<html lang="en">
<head>
<meta charset="utf-8">
<title>Pelvoran Concept and Envisioned Project Progression</title>
<link rel="stylesheet" href="https://fonts.googleapis.com/css2?family=Josefin+Sans:wght@600;700&family=Roboto+Condensed:wght@700&display=swap">
<style>
  :root{
    --stage:#6b6b6b;
    --green:#0fd35c;
    --green-deep:#00c04b;
    --green-soft:#8ee08e;
    --brown:#8a6a00;
    --brown-dark:#5e4700;
    --ink:#111;
    --paper:#fff;
    --night:#000;
  }
  html,body{margin:0;padding:0;width:1200px;height:1000px;overflow:hidden;background:var(--stage);}
  .canvas{position:relative;width:1200px;height:1000px;}
  .panel{position:absolute;top:152px;height:695px;}
  .panel--light{left:40px;width:557px;background:var(--paper);--text:var(--ink);--step-text:var(--ink);--inhibit:#bff0cf;}
  .panel--dark{left:604px;width:555px;background:var(--night);--text:var(--paper);--step-text:var(--paper);--inhibit:var(--green);}
  .panel svg{display:block;width:557px;height:695px;}
  .title-box{fill:var(--green-soft);stroke:var(--green-deep);stroke-width:4;}
  .panel--dark .title-box{fill:var(--green);stroke:var(--green-soft);}
  .title-text{font-family:"Roboto Condensed",sans-serif;font-weight:700;font-size:17px;letter-spacing:1.6px;fill:var(--ink);}
  .panel--dark .title-text{fill:var(--paper);}
  .force-pill{fill:var(--green);}
  .force-label{font-family:"Josefin Sans",sans-serif;font-weight:700;font-size:16px;letter-spacing:1px;fill:var(--ink);}
  .panel--dark .force-label{fill:var(--paper);}
  .force-circle{fill:var(--green-soft);stroke:var(--green-deep);stroke-width:4;}
  .micro-view{stroke:var(--green);stroke-width:7;}
  .badge-text{font-family:"Josefin Sans",sans-serif;font-weight:600;font-size:11.5px;fill:var(--ink);}
  .panel--dark .badge-text{fill:var(--paper);}
  .box-text{font-family:"Josefin Sans",sans-serif;font-weight:600;font-size:12.5px;fill:var(--ink);}
  .panel--dark .box-text{fill:var(--paper);}
  .outcome-text{font-family:"Josefin Sans",sans-serif;font-weight:600;font-size:18px;letter-spacing:1px;fill:var(--ink);}
  .panel--dark .outcome-text{fill:var(--paper);}
  .green-fill{fill:var(--green);}
  .flow-line{stroke:var(--green);stroke-width:5;}
  .inhibit-line{stroke:var(--inhibit);stroke-width:5;}
  .brown-line{stroke:var(--brown);stroke-width:5;}
  .panel--dark .brown-line{stroke:var(--green);}
  .panel--dark .brown-head{fill:var(--green);}
  .brown-head{fill:var(--brown);}
  .chip{fill:var(--brown);stroke:var(--paper);stroke-width:1.2;}
  .step-pill{fill:var(--green);}
  .step-text{font-family:"Josefin Sans",sans-serif;font-weight:700;font-size:19px;letter-spacing:1.2px;fill:var(--step-text);}
</style>
</head>
<body>
<main class="canvas">

  <!-- shared artwork definition, used by both versions -->
  <svg width="0" height="0" style="position:absolute" aria-hidden="true">
    <defs>
      <linearGradient id="decline" x1="0" x2="1" y1="0" y2="0">
        <stop offset="0" stop-color="#0fd35c"/>
        <stop offset="0.45" stop-color="#9a8a00"/>
        <stop offset="1" stop-color="#6a5000"/>
      </linearGradient>
      <linearGradient id="decline-solid" x1="0" x2="1">
        <stop offset="0" stop-color="#8a6a00"/>
        <stop offset="1" stop-color="#5e4700"/>
      </linearGradient>
      <radialGradient id="micro" cx="0.5" cy="0.5" r="0.6">
        <stop offset="0" stop-color="#3e6a2a"/>
        <stop offset="0.6" stop-color="#1f3d18"/>
        <stop offset="1" stop-color="#0c1a0a"/>
      </radialGradient>
      <g id="concept">
        <rect class="title-box" x="15" y="20" width="525" height="45"/>
        <text class="title-text" x="277" y="49" text-anchor="middle">Pelvoran Concept and Envisioned Project Progression</text>

        <rect class="force-pill" x="16" y="84" width="115" height="23" rx="11.5"/>
        <text class="force-label" x="73" y="101" text-anchor="middle">Pressure</text>
        <rect class="force-pill" x="150" y="84" width="115" height="23" rx="11.5"/>
        <text class="force-label" x="207" y="101" text-anchor="middle">Shear</text>
        <rect class="force-pill" x="283" y="84" width="125" height="23" rx="11.5"/>
        <text class="force-label" x="345" y="101" text-anchor="middle">Tension</text>
        <rect class="force-pill" x="425" y="84" width="116" height="23" rx="11.5"/>
        <text class="force-label" x="483" y="101" text-anchor="middle">Strain</text>

        <circle class="force-circle" cx="74" cy="183" r="63" role="img" aria-label="Cell squeezed by pressure from above"/>
        <circle class="force-circle" cx="208" cy="183" r="63" role="img" aria-label="Cell pushed by shear flow"/>
        <circle class="force-circle" cx="345" cy="183" r="63" role="img" aria-label="Cell pulled upward by tension"/>
        <circle class="force-circle" cx="482" cy="183" r="63" role="img" aria-label="Cell stretched by strain"/>

        <polygon class="green-fill" points="175,245 199,255 208,278 199,301 175,311 151,301 142,278 151,255"/>
        <text class="badge-text" x="175" y="276" text-anchor="middle">Cell</text>
        <text class="badge-text" x="175" y="292" text-anchor="middle">Fitness</text>

        <polygon fill="url(#decline)" points="377,242 384,258 399,252 396,268 412,272 400,282 410,295 394,296 394,312 381,303 370,314 365,299 349,300 357,286 344,278 359,270 354,255 369,259"/>
        <text class="badge-text" x="378" y="276" text-anchor="middle">Cell</text>
        <text class="badge-text" x="378" y="292" text-anchor="middle">Frailty</text>

        <circle class="micro-view" cx="278" cy="338" r="67" fill="url(#micro)" role="img" aria-label="Fluorescence microscopy view of cultured cells"/>

        <rect class="green-fill" x="26" y="312" width="111" height="77"/>
        <text class="box-text" x="81" y="336" text-anchor="middle">Functional</text>
        <text class="box-text" x="81" y="354" text-anchor="middle">Cellular</text>
        <text class="box-text" x="81" y="372" text-anchor="middle">Machineries</text>

        <line class="flow-line" x1="196" y1="341" x2="164" y2="341"/>
        <polygon class="green-fill" points="152,341 166,332 166,350"/>

        <rect fill="url(#decline)" x="415" y="312" width="115" height="77"/>
        <rect class="chip" x="495" y="304" width="15" height="15"/>
        <rect class="chip" x="511" y="304" width="15" height="15"/>
        <rect class="chip" x="511" y="320" width="15" height="15"/>
        <text class="box-text" x="472" y="334" text-anchor="middle">Dysfunctional</text>
        <text class="box-text" x="472" y="352" text-anchor="middle">Cellular</text>
        <text class="box-text" x="472" y="370" text-anchor="middle">Machineries</text>

        <line class="inhibit-line" x1="405" y1="341" x2="368" y2="341"/>
        <line class="inhibit-line" x1="368" y1="328" x2="368" y2="356"/>

        <line class="flow-line" x1="82" y1="395" x2="82" y2="423"/>
        <polygon class="green-fill" points="82,438 73,422 91,422"/>
        <rect class="green-fill" x="26" y="443" width="111" height="43"/>
        <text class="outcome-text" x="81" y="472" text-anchor="middle">Health</text>

        <line class="brown-line" x1="478" y1="395" x2="478" y2="423"/>
        <polygon class="brown-head" points="478,438 469,422 487,422"/>
        <rect fill="url(#decline-solid)" x="422" y="443" width="113" height="43"/>
        <rect class="chip" x="507" y="438" width="14" height="14"/>
        <rect class="chip" x="522" y="438" width="14" height="14"/>
        <rect class="chip" x="522" y="453" width="14" height="14"/>
        <text class="outcome-text" x="476" y="472" text-anchor="middle">Disease</text>

        <rect class="step-pill" x="202" y="414" width="152" height="32" rx="16"/>
        <text class="step-text" x="278" y="437" text-anchor="middle">Therapies</text>
        <rect class="step-pill" x="197" y="452" width="161" height="32" rx="16"/>
        <text class="step-text" x="278" y="475" text-anchor="middle">prevention</text>
        <rect class="step-pill" x="181" y="489" width="194" height="33" rx="16"/>
        <text class="step-text" x="278" y="512" text-anchor="middle">Critical Targets</text>
        <rect class="step-pill" x="168" y="527" width="220" height="33" rx="16"/>
        <text class="step-text" x="278" y="550" text-anchor="middle">Cellular Machineries</text>
        <rect class="step-pill" x="168" y="565" width="219" height="32" rx="16"/>
        <text class="step-text" x="278" y="588" text-anchor="middle">Disease Models</text>
        <rect class="step-pill" x="79" y="602" width="399" height="33" rx="16"/>
        <text class="step-text" x="278" y="625" text-anchor="middle">Cell, Tissues &amp; Organ Responses</text>
        <rect class="step-pill" x="113" y="640" width="330" height="34" rx="17"/>
        <text class="step-text" x="278" y="664" text-anchor="middle">Mechanical Forces Models</text>
      </g>
    </defs>
  </svg>

  <section class="panel panel--light" aria-label="Concept figure, white background">
    <svg viewBox="0 0 557 695"><use href="#concept"/></svg>
  </section>

  <section class="panel panel--dark" aria-label="Concept figure, black background">
    <svg viewBox="0 0 557 695"><use href="#concept"/></svg>
  </section>

</main>
</body>
</html>
```